Webdesign für WBG Haselgrund
Zielgruppe
Die Wohnungsgesellschaft Haselgrund mbH ist der Dienstleister für mehr Freude am Wohnen im schönen Muldental,
in Rochlitz, Penig und Wechselburg.
Die Wohnungsvielfalt in Rochlitz, Penig und Wechselburg reicht von saniertem Altbau bis zu modernem Neubau, von klein bis groß und von zweckmäßig bis großzügig-komfortabel, kinderfreundlich und auch seniorengerecht.
Zielgruppe: Jung bis Alt - Fokus eher auf Ältere in den o.g. Städten
die Vermietung von Wohnungen steht im Vordergrund
Aufgabenstellung
- Slogan derzeit'...mehr Freude am Wohnen' soll nicht mehr verwendet werden - kreative Ideen von Ihnen gefragt
- Schnelle Kontaktaufnahme der Kundenbetreuung in Rochlitz und Penig/ Wechselburg
- im footer sollen die 3 Geschäftstellen inkl. Kontaktdaten und Sprechzeiten stehen
- alle Navigationspunkte sollten ein Segment erhalten
- 'Aktuelles' und 'Aktionen' sollten herausstechen,
- das Logo wurde neu erstellt - die Farben der Webseite analog + eine weitere Farbe ( hier sind wir offen) , allerdings nicht zu bunt

```html
<!DOCTYPE html>
<html lang="de">
<head>
<meta charset="utf-8">
<title>WBG Haselgrund – Wohnen in Rochlitz, Penig und Wechselburg</title>
<link href="https://fonts.googleapis.com/css2?family=Karla:wght@400;500;700&display=swap" rel="stylesheet">
<style>
:root{
  --brand:#a0005a;
  --accent:#c8944a;
  --ink:#1b1b1b;
  --muted:#555;
  --band:#f5f5f5;
  --line:#d8d8d8;
  --white:#fff;
}
*{box-sizing:border-box;margin:0;padding:0}
html,body{width:1200px;height:3125px;overflow:hidden}
body{position:relative;font-family:"Karla",Arial,sans-serif;color:var(--ink);background:var(--white)}
.abs{position:absolute}
a{color:inherit;text-decoration:none}

/* header */
.brand{left:235px;top:44px;display:flex;align-items:center;gap:10px;font-weight:700;font-size:22px;color:var(--brand)}
.brand-mark{width:18px;height:18px;background:var(--brand)}
.nav{left:559px;top:47px;display:flex;gap:29px;font-size:12.5px;font-weight:500;z-index:2}
.nav a.active{color:var(--accent);border-bottom:2px solid var(--accent);padding-bottom:3px}

/* hero */
.hero-photo{left:560px;top:0;width:640px;height:510px;background:linear-gradient(100deg,rgba(255,255,255,1) 0%,rgba(235,238,242,.8) 25%,#dfe4ea 55%,#b9c4cf 100%)}
.hero-glow{left:100px;top:260px;width:460px;height:250px;background:radial-gradient(ellipse at 30% 60%,#fdfaf1 0%,rgba(255,255,255,0) 70%)}
.hero-title{left:235px;top:180px;font-size:25px;font-weight:500;line-height:1.1}
.hero-text{left:235px;top:257px;width:320px;font-size:10.5px;line-height:1.22;color:#333}
.btn{display:inline-flex;align-items:center;justify-content:center;gap:6px;background:var(--brand);color:var(--white);font-size:11px;font-weight:500;border-radius:2px}
.hero-btn{left:236px;top:349px;width:126px;height:36px}
.quick{left:1162px;top:223px;width:38px;display:flex;flex-direction:column;gap:2px}
.quick span{height:38px;background:var(--accent);display:flex;align-items:center;justify-content:center}

/* sections */
h2{font-size:27px;font-weight:500}
.band{left:0;width:1200px;background:var(--band)}
.listing-title{left:235px;top:546px}
.all-btn{left:854px;top:550px;width:111px;height:35px}
.tabs{left:235px;top:613px;display:flex;font-size:12px}
.tabs span{margin-right:32px}
.tabs .active{color:var(--accent);border-bottom:2px solid var(--accent);padding-bottom:3px}
.card{width:235px}
.card .photo{width:235px;height:187px;background:linear-gradient(180deg,#6d9fd6 0%,#b8d2ea 45%,#dad6cc 70%,#7d8a63 100%);position:relative}
.card h3{margin-top:9px;font-size:11.5px;font-weight:700}
.card p{margin-top:6px;font-size:8.6px;color:var(--muted)}
.card.hover h3{color:var(--accent)}
.photo .go{position:absolute;left:62px;top:78px;width:110px;height:34px}

.about-photo{left:235px;top:1258px;width:296px;height:317px;background:linear-gradient(180deg,#3f86c9 0%,#9ec4e6 30%,#eef0f2 55%,#dcdcdc 80%,#5d6b47 100%)}
.about{left:607px;top:1310px;width:360px}
.about p{margin-top:12px;font-size:12px;line-height:1.45;color:#333}
.about h2{margin-bottom:8px}
.more{display:flex;align-items:center;gap:8px;margin-top:14px;font-size:12px;font-weight:700}

.intro{font-size:12px;line-height:1.45;color:#333;width:540px;margin-top:12px}
.valley{left:235px;top:1712px}
.sights{left:235px;top:1841px;display:flex;gap:13px}
.sight{width:173px}
.sight .photo{height:138px;background:linear-gradient(180deg,#9fbedc 0%,#d6e0e8 35%,#8d9a7a 60%,#3f5e2c 100%)}
.sight span{display:block;margin-top:8px;font-size:12px;font-weight:500}

.downloads{left:235px;top:2155px}
.dl-list{left:234px;top:2268px;width:731px}
.dl-row{display:flex;justify-content:space-between;align-items:center;height:55px;border-bottom:1px solid var(--line);font-size:12px}
.dl-row .btn{width:110px;height:35px}

.cta{left:235px;top:2584px;width:730px;height:175px;background:var(--brand);color:var(--white);padding:55px 50px 0;overflow:hidden}
.cta h2{font-weight:500}
.cta p{margin-top:8px;font-size:16px;line-height:1.2}

.footer{top:2840px;height:249px}
.office{top:2878px;width:230px;font-size:8.8px;line-height:1.38;color:#222}
.office h4{font-size:10px;font-weight:700;margin-bottom:4px}
.office .gap{height:14px}
.office .row{display:flex}
.office .row b{font-weight:400;width:52px}
.office .icon{display:flex;align-items:center;gap:4px}
.legal{left:235px;top:3102px;font-size:8px;font-weight:700}
</style>
</head>
<body>

<header>
  <div class="abs brand"><span class="brand-mark"></span>WBG Haselgrund</div>
  <nav class="abs nav">
    <a class="active">Wohnungen</a><a>Aktuelles</a><a>Tourismus</a><a>Downloads</a><a>Kontakt</a>
  </nav>
</header>

<section>
  <div class="abs hero-glow"></div>
  <div class="abs hero-photo" role="img" aria-label="Moderne weiße Wohnhausfassade mit Balkonen"></div>
  <h1 class="abs hero-title">Wohnen in Rochlitz,<br>Penig und Wechselburg</h1>
  <div class="abs hero-text">
    <p>Bei uns finden Sie als Interessenten, Mieter oder Eigentümer das Richtige.</p>
    <p>Unsere Wohnungsvielfalt in Rochlitz, Penig und Wechselburg reicht von saniertem Altbau bis zu modernem Neubau, von klein bis groß und von zweckmäßig bis großzügig-komfortabel.</p>
  </div>
  <a class="abs btn hero-btn">Zu den Wohnungen</a>
  <div class="abs quick">
    <span><svg width="18" height="18" viewBox="0 0 18 18"><path d="M9 2 1 9h2v7h4v-5h4v5h4V9h2z" fill="#fff"/></svg></span>
    <span><svg width="18" height="14" viewBox="0 0 18 14"><rect x="1" y="1" width="16" height="12" fill="#fff"/><path d="M1 1l8 6 8-6" stroke="#c8944a" stroke-width="1.4" fill="none"/></svg></span>
    <span><svg width="18" height="18" viewBox="0 0 18 18"><circle cx="9" cy="9" r="8" fill="#fff"/><path d="M9 4v5h4" stroke="#c8944a" stroke-width="1.6" fill="none"/></svg></span>
  </div>
</section>

<section>
  <h2 class="abs listing-title">Aktuelle Wohnungen</h2>
  <a class="abs btn all-btn">Alle Wohnungen</a>
  <div class="abs tabs"><span class="active">Rochlitz</span><span>Penig</span><span>Wechselburg</span><span>Seniorengerecht</span><span>Ortsteil Amerika</span></div>

  <article class="abs card" style="left:235px;top:665px"><div class="photo" role="img" aria-label="Mehrfamilienhaus mit Balkonen"></div><h3>4-Raumwohnung mit Balkon</h3><p>67,9m² | Kaltmiete 340,00€ | Nebenkosten: 68,00€</p></article>
  <article class="abs card" style="left:483px;top:665px"><div class="photo" role="img" aria-label="Wohnhaus mit Satteldach"></div><h3>2-Raumwohnung</h3><p>47,86m² | Kaltmiete 240,00€ | Nebenkosten: 60,00€</p></article>
  <article class="abs card hover" style="left:730px;top:665px"><div class="photo" role="img" aria-label="Neubau mit Balkonen"><a class="btn go">Zur Immobilie</a></div><h3>3-Raumwohnung mit Balkon</h3><p>56,7m² | Kaltmiete 284,00€ | Nebenkosten: 60,00€</p></article>
  <article class="abs card" style="left:235px;top:926px"><div class="photo" role="img" aria-label="Villa am Wasser mit Bäumen"></div><h3>3-Raumwohnung mit Balkon</h3><p>56,7m² | Kaltmiete 284,00€ | Nebenkosten: 60,00€</p></article>
  <article class="abs card" style="left:483px;top:926px"><div class="photo" role="img" aria-label="Altstadthäuser am Fluss"></div><h3>3-Raumwohnung mit Balkon</h3><p>56,7m² | Kaltmiete 284,00€ | Nebenkosten: 60,00€</p></article>
  <article class="abs card" style="left:730px;top:926px"><div class="photo" role="img" aria-label="Moderne Wohnanlage mit Balkonen"></div><h3>1-Raum Singlewohnung mit Balkon</h3><p>64,12m² | Kaltmiete 324,00€ | Nebenkosten: 64,00€</p></article>
</section>

<section>
  <div class="abs band" style="top:1210px;height:422px"></div>
  <div class="abs about-photo" role="img" aria-label="Weißes modernes Mehrfamilienhaus"></div>
  <div class="abs about">
    <h2>Über uns</h2>
    <p>Die Wohnungsgesellschaft Haselgrund mbH wurde im Jahr 2006 durch Fusion der Baugenossenschaft Lindenhof mbH, der Wohnbau Talblick mbH und der Hausverwaltung Auenweg mbH gegründet.</p>
    <p>Aktuell bewirtschaftet unser Team 940 Wohnungen und mehrere Gewerbeeinheiten an den Standorten Rochlitz, Penig und Wechselburg .</p>
    <a class="more">Erfahre mehr <svg width="14" height="8" viewBox="0 0 14 8"><path d="M0 4h12M9 1l3 3-3 3" stroke="#1b1b1b" stroke-width="1.4" fill="none"/></svg></a>
  </div>
</section>

<section>
  <div class="abs valley">
    <h2>Das Tal der Burgen, Schlösser und Klöster</h2>
    <p class="intro">Weit hinten, hinter den Wortbergen, fern der Länder Vokalien und Konsonantien leben die Blindtexte. Abgeschieden wohnen sie in Buchstabhausen an der Küste des Semantik, eines großen Sprachozeans.</p>
  </div>
  <div class="abs sights">
    <div class="sight"><div class="photo" role="img" aria-label="Schloss auf bewaldetem Hügel"></div><span>Schloß Rochsburg</span></div>
    <div class="sight"><div class="photo" role="img" aria-label="Schloss mit zwei Türmen"></div><span>Schloß Rochlitz</span></div>
    <div class="sight"><div class="photo" role="img" aria-label="Romanische Klosterkirche"></div><span>Kloster Wechselburg</span></div>
    <div class="sight"><div class="photo" role="img" aria-label="Schloss über Baumkronen"></div><span>Schloss Wolkenburg</span></div>
  </div>
</section>

<section>
  <div class="abs band" style="top:2082px;height:422px"></div>
  <div class="abs downloads">
    <h2>Downloads</h2>
    <p class="intro">Weit hinten, hinter den Wortbergen, fern der Länder Vokalien und Konsonantien leben die Blindtexte. Abgeschieden wohnen sie in Buchstabhausen an der Küste des Semantik, eines großen Sprachozeans.</p>
  </div>
  <div class="abs dl-list">
    <div class="dl-row"><span>Unternehmensbroschüre.pdf</span><a class="btn"><svg width="10" height="11" viewBox="0 0 10 11"><path d="M5 0v7M2 4l3 3 3-3M0 10h10" stroke="#fff" stroke-width="1.6" fill="none"/></svg>Downloaden</a></div>
    <div class="dl-row"><span>Beispielname.pdf</span><a class="btn"><svg width="10" height="11" viewBox="0 0 10 11"><path d="M5 0v7M2 4l3 3 3-3M0 10h10" stroke="#fff" stroke-width="1.6" fill="none"/></svg>Downloaden</a></div>
    <div class="dl-row"><span>Noch-eine-Datei.pdf</span><a class="btn"><svg width="10" height="11" viewBox="0 0 10 11"><path d="M5 0v7M2 4l3 3 3-3M0 10h10" stroke="#fff" stroke-width="1.6" fill="none"/></svg>Downloaden</a></div>
  </div>
</section>

<section class="abs cta">
  <h2>Mieter werben Mieter</h2>
  <p>Für jeden durch Ihre Empfehlung abgeschlossenen<br>Mietvertrag erhalten Sie 200,00 €</p>
</section>

<footer>
  <div class="abs band footer"></div>
  <div class="abs office" style="left:235px">
    <h4>Geschäftsstelle Rochlitz</h4>
    <p>Lindenstr. 14<br>09306 Rochlitz<br>Tel. 03737 / 55 20 10<br>Fax 03737 / 55 20 19</p>
    <div class="gap"></div>
    <h4>Sprechzeiten</h4>
    <div class="row"><b>Montag:</b>09:00 - 12:00 Uhr</div>
    <div class="row"><b>Dienstag:</b>13:00 - 18:00 Uhr</div>
    <div class="row"><b>Donnerstag:</b>13:00 - 16:00 Uhr</div>
    <div class="gap"></div>
    <div class="icon"><svg width="8" height="8" viewBox="0 0 8 8"><path d="M1 0h2l1 2-1 1c.5 1 1 1.5 2 2l1-1 2 1v2c-4 0-7-3-7-7z" fill="#222"/></svg>03737 55 20 10</div>
    <div class="icon"><svg width="8" height="8" viewBox="0 0 8 8"><rect x="2" y="0" width="4" height="3" fill="#222"/><rect x="0" y="3" width="8" height="4" fill="#222"/></svg>03737 55 20 19</div>
  </div>
  <div class="abs office" style="left:483px">
    <h4>Vermietungsbüro Penig</h4>
    <p>Am Markt 9<br>09322 Penig<br>Tel. 037381 / 4420<br>Fax 037381 / 4429</p>
    <div class="gap"></div>
    <h4>Sprechzeiten</h4>
    <div class="row"><b>Montag:</b>09:00 - 12:00 Uhr</div>
    <div class="row"><b>Dienstag:</b>13:00 - 18:00 Uhr</div>
    <div class="row"><b>Donnerstag</b>09:00 - 11:00 Uhr</div>
    <div class="gap"></div>
    <div class="icon"><svg width="8" height="8" viewBox="0 0 8 8"><path d="M1 0h2l1 2-1 1c.5 1 1 1.5 2 2l1-1 2 1v2c-4 0-7-3-7-7z" fill="#222"/></svg>037381 44 20</div>
    <div class="icon"><svg width="8" height="8" viewBox="0 0 8 8"><rect x="2" y="0" width="4" height="3" fill="#222"/><rect x="0" y="3" width="8" height="4" fill="#222"/></svg>037381 44 29</div>
  </div>
  <div class="abs office" style="left:730px">
    <h4>Vermietungsbüro Wechselburg</h4>
    <p>Gartenweg 3<br>09306 Wechselburg<br>Tel. 037384 / 3350</p>
    <div class="gap"></div>
    <div class="gap"></div>
    <h4>Sprechzeiten</h4>
    <div>Donnerstag: 14:00 - 17:00 Uhr</div>
    <div class="gap"></div>
    <div class="gap"></div>
    <div class="icon" style="margin-top:5px"><svg width="8" height="8" viewBox="0 0 8 8"><path d="M1 0h2l1 2-1 1c.5 1 1 1.5 2 2l1-1 2 1v2c-4 0-7-3-7-7z" fill="#222"/></svg>037384 3350 (zur Sprechzeit)</div>
  </div>
  <div class="abs legal">Impressum &nbsp;|&nbsp; Datenschutzerklärung</div>
</footer>

</body>
</html>
```